Salt Water Delivery Company Business Card Design

We are a company that delivers natural saltwater (from the ocean) to aquarium companies, restaurants and home marine tanks. I would like a new business card to suit.

Must include Name, company name, abn, contact number and website as well as logo (see attached).

Looking for a design that stands out, has a clean but unique appearance.

Double and single sided entries welcome

Industry/Entity Type

Business

Requirements
Must have
• Logo

```html
<!DOCTYPE html>
<html lang="en">
<head>
<meta charset="utf-8">
<title>BrineRun Business Card</title>
<link rel="stylesheet" href="https://fonts.googleapis.com/css2?family=Source+Sans+3:ital,wght@0,400;0,600;0,700;1,700&display=swap">
<style>
  :root {
    --backdrop: #1c1c1c;
    --paper: #ffffff;
    --brand-blue: #0b5eae;
    --sky-blue: #3ab0e6;
    --text-white: #ffffff;
  }
  * { box-sizing: border-box; margin: 0; padding: 0; }
  html, body {
    width: 1200px;
    height: 420px;
    overflow: hidden;
  }
  body {
    background: var(--backdrop);
    font-family: "Source Sans 3", sans-serif;
    position: relative;
  }
  .card {
    position: absolute;
    top: 62px;
    width: 522px;
    height: 300px;
    border-radius: 16px;
    overflow: hidden;
  }
  .card--front { left: 68px; background: var(--paper); }
  .card--back { left: 630px; background: var(--brand-blue); }

  .brand {
    position: absolute;
    left: 0;
    width: 100%;
    text-align: center;
  }
  .brand__name {
    display: block;
    font-weight: 600;
    line-height: 1;
  }
  .brand__tagline {
    display: block;
    font-weight: 700;
    font-style: italic;
    line-height: 1;
  }
  .card--front .brand { top: 78px; }
  .card--front .brand__name { color: var(--sky-blue); font-size: 44px; }
  .card--front .brand__tagline { color: var(--brand-blue); font-size: 17px; margin-top: 4px; }

  .card--back .brand { top: 128px; }
  .card--back .brand__name { color: var(--text-white); font-size: 78px; }
  .card--back .brand__tagline { color: var(--text-white); font-size: 27px; margin-top: 0; }

  .contact-band {
    position: absolute;
    left: 0;
    top: 166px;
    width: 100%;
    height: 86px;
    background: var(--brand-blue);
    color: var(--text-white);
  }
  .person {
    position: absolute;
    right: 296px;
    top: 20px;
    text-align: right;
  }
  .person__name { font-size: 18px; font-weight: 700; line-height: 1.2; }
  .person__title { font-size: 15px; line-height: 1.4; }
  .contact-band__divider {
    position: absolute;
    left: 238px;
    top: 10px;
    width: 1.5px;
    height: 66px;
    background: var(--text-white);
  }
  .contact-list {
    position: absolute;
    left: 252px;
    top: 20px;
    list-style: none;
    font-size: 15.5px;
  }
  .contact-list li {
    display: flex;
    align-items: center;
    gap: 7px;
    line-height: 24px;
  }
  .contact-list svg { width: 12px; height: 12px; }

  .address {
    position: absolute;
    left: 0;
    top: 260px;
    width: 100%;
    text-align: center;
    color: var(--brand-blue);
    font-size: 13.5px;
    line-height: 19px;
  }
</style>
</head>
<body>
  <section class="card card--front">
    <div class="brand">
      <span class="brand__name">BrineRun</span>
      <span class="brand__tagline">Saltwater Deliveries</span>
    </div>

    <div class="contact-band">
      <div class="person">
        <p class="person__name">Your Name</p>
        <p class="person__title">Title</p>
      </div>
      <div class="contact-band__divider"></div>
      <ul class="contact-list">
        <li>
          <svg viewBox="0 0 12 12" aria-hidden="true"><path d="M2.5 1 L4.5 1 L5 3.5 L3.8 4.4 Q4.8 6.6 7.4 8.2 L8.4 7 L11 7.6 L11 9.6 Q10.6 11 9 11 Q1 10 1 2.6 Q1 1 2.5 1 Z" fill="#ffffff"/></svg>
          <span>123-456-7892</span>
        </li>
        <li>
          <svg viewBox="0 0 12 12" aria-hidden="true"><g fill="none" stroke="#ffffff" stroke-width="1"><circle cx="6" cy="6" r="5"/><ellipse cx="6" cy="6" rx="2.2" ry="5"/><line x1="1" y1="6" x2="11" y2="6"/></g></svg>
          <span>www.brinerun.com</span>
        </li>
      </ul>
    </div>

    <p class="address">Street Name, City Name ,State, Zip Code<br>ABN: 123456789</p>
  </section>

  <section class="card card--back">
    <div class="brand">
      <span class="brand__name">BrineRun</span>
      <span class="brand__tagline">Saltwater Deliveries</span>
    </div>
  </section>
</body>
</html>
```